Legal Information Website

We need a website that will serve as a source of information for people visiting, living, and working in the United Arab Emirates, where they can go and read about legal issues, laws, crimes, and most important find legal advice and find lawyers. The following are the pages of the website:

Find a Lawyer (Home Page)
This main feature of this page should be "Find a Lawyer"
Find a Lawyer should include the searching option by practice, by lawyer’s name, by law firm name or by location.

Ask a lawyer
This function allows the user to ask a lawyer a legal question and get an answer directly from a lawyer.

Research a legal matter
This function allows the user to do research on a certain legal topic. He/she can select from different legal topics.

Contact Us:
This page should include our contact details for the visitors in case they need any assistance. Contact us by Phone, Email, or Chat.

Once the design is approved, we will provide the rest of the website text.

Target Market(s)

General Public who seek legal advice

Industry/Entity Type

Law Firm

Font styles to use
Serif
Sans Serif

Requirements
Must have
• A tool to search for lawyer's, and then display the lawyer's picture and profile and credentials.

```html
<!DOCTYPE html>
<html lang="en">
<head>
<meta charset="utf-8">
<title>Cedar Group – Legal Information</title>
<link href="https://fonts.googleapis.com/css2?family=Open+Sans:wght@400;600;700&family=Tinos&family=Arimo&display=swap" rel="stylesheet">
<style>
:root{
  --red:#8c2a1f;
  --red-dark:#6e1e15;
  --ink:#333333;
  --muted:#555555;
  --band:#dcdcdc;
  --news-bg:#efefef;
  --footer:#3a3a3a;
  --white:#ffffff;
  --btn-dark:#3d3d3d;
}
*{box-sizing:border-box;margin:0;padding:0}
html,body{width:1110px;height:1200px;overflow:hidden;background:var(--white)}
body{position:relative;font-family:"Open Sans",sans-serif;color:var(--ink)}
.abs{position:absolute}

/* header */
.brand{left:166px;top:24px;width:106px;height:80px;background:#f4f4f4;display:flex;align-items:center;justify-content:center;gap:6px}
.brand-name{font-size:17px;font-weight:600;color:#222;letter-spacing:.5px}
.brand-dot{width:10px;height:10px;background:var(--red)}
.top-links{right:160px;top:34px;display:flex;gap:22px;font-size:13px;color:var(--muted);align-items:center}
.top-links span{display:flex;align-items:center;gap:7px}
.main-nav{right:160px;top:72px;display:flex;gap:16px;font-size:13px;text-transform:uppercase;color:var(--ink);align-items:center}
.main-nav a{color:inherit;text-decoration:none;padding:3px 6px}
.main-nav a.active{border:2px solid var(--red);color:var(--red)}

/* hero */
.hero-photo{left:0;top:112px;width:1110px;height:355px;background:linear-gradient(180deg,#a9c6e6 0%,#d9d2c4 35%,#c9b49a 70%,#9c7f62 100%)}
.hero-title{left:160px;top:122px;font-size:34px;color:#222}
.finder{left:744px;top:165px;width:204px;height:236px;background:rgba(80,80,80,.82);border-radius:5px;padding:14px 15px 0}
.finder h2{font-size:15px;color:var(--white);text-align:center;font-weight:600;margin-bottom:8px}
.field{display:flex;height:25px;margin-bottom:15px;border-radius:4px;overflow:hidden}
.field i{width:25px;background:var(--red);display:flex;align-items:center;justify-content:center}
.field span{flex:1;background:var(--white);font-size:8px;color:#333;display:flex;align-items:center;padding-left:8px}
.search-btn{display:block;margin:2px auto 0;width:104px;height:24px;border-radius:12px;background:#222;color:var(--white);font-size:13px;font-weight:600;text-align:center;line-height:24px}
.slider-ctrl{left:470px;top:432px;width:164px;height:27px;background:#eef0f3;border:1px solid #bbb;border-radius:4px;display:flex;align-items:center;padding:0 10px;gap:7px}
.dot{width:8px;height:8px;border-radius:50%;background:#aaa}
.dot.on{background:#333}

/* offer */
.offer{left:0;top:484px;width:1110px;text-align:center;font-family:"Tinos",serif}
.offer h1{font-size:19px;font-weight:400;color:#222}
.offer h1 em{font-style:normal;color:var(--red)}
.offer p{font-size:14px;color:#777;margin-top:8px}
.btn{display:inline-block;color:var(--white);font-size:11px;font-weight:600;text-align:center;border-radius:3px;text-transform:uppercase}
.btn-dark{background:linear-gradient(#555,#2e2e2e);border:1px solid #222}
.btn-red{background:linear-gradient(#a23c2e,var(--red-dark));border:1px solid #5a160f}
.cta-learn{left:402px;top:555px;width:111px;height:32px;line-height:30px}
.cta-or{left:530px;top:563px;font-family:"Tinos",serif;font-size:13px;color:#555}
.cta-join{left:585px;top:555px;width:111px;height:32px;line-height:30px}

/* features */
.band{left:0;top:598px;width:1110px;height:174px;background:var(--band)}
.feature{top:626px;width:190px}
.feature h3{font-size:18px;font-weight:400;color:#333;display:flex;align-items:center;gap:8px;margin-bottom:10px;white-space:nowrap}
.feature p{font-family:"Arimo",sans-serif;font-size:9.5px;line-height:14.4px;color:#444;text-align:justify}
.feature .btn{margin-top:6px;width:76px;height:26px;line-height:24px;font-size:10px}

/* solutions */
.section-title{font-size:18px;font-weight:600;color:#333}
.solutions-photo{left:158px;top:827px;width:396px;height:152px;background:linear-gradient(90deg,#3a2a22 0%,#5a4437 45%,#cfc8bc 75%,#e9e5dd 100%)}
.solutions-text{left:158px;top:988px;width:396px;font-family:"Arimo",sans-serif;font-size:12px;line-height:20px;color:#444;text-align:justify}
.sol-btn{left:476px;top:1030px;width:77px;height:26px;line-height:24px;font-size:10px}

/* news */
.news-box{left:580px;top:816px;width:373px;height:238px;background:var(--news-bg)}
.news-item{left:596px;display:flex;gap:9px}
.news-thumb{width:112px;height:57px}
.news-item h4{font-family:"Arimo",sans-serif;font-weight:400;font-size:13px;color:var(--red-dark);margin-bottom:3px}
.news-item p{font-family:"Arimo",sans-serif;font-size:11.5px;line-height:20px;color:#333}

/* footer */
.footer{left:0;top:1073px;width:1110px;height:127px;background:var(--footer);color:var(--white)}
.footer-links{left:0;top:1088px;width:1110px;text-align:center;font-size:11.5px;color:var(--white)}
.copyright{left:158px;top:1134px;font-family:"Arimo",sans-serif;font-size:10px;color:var(--white)}
.social{left:470px;top:1124px;display:flex;gap:11px}
.social span{width:26px;height:26px;border-radius:50%;border:2px solid #222}
.newsletter{left:760px;top:1125px;width:192px;height:24px;background:var(--white);font-family:"Arimo",sans-serif;font-style:italic;font-size:10px;color:#777;padding-left:8px;line-height:24px}
</style>
</head>
<body>

<header>
  <div class="abs brand"><span class="brand-dot"></span><span class="brand-name">Cedar Group</span></div>
  <div class="abs top-links">
    <span><svg width="16" height="16"><rect width="16" height="16" rx="3" fill="#8c2a1f"/><path d="M5 4c1 0 1.5 2 1 2.5s0 2 1.5 3.5 3 2 3.5 1.5 2.5 0 2.5 1-1 2-2 1.5C8 12 4 8 4 5c0-.5.5-1 1-1z" fill="#fff"/></svg>+971 4 555 0182</span>
    <span><svg width="17" height="17"><circle cx="8.5" cy="8.5" r="7.5" fill="none" stroke="#8c2a1f" stroke-width="2"/><path d="M5 8.5h6M8.5 5.5l3 3-3 3" fill="none" stroke="#8c2a1f" stroke-width="2"/></svg>Register</span>
    <span><svg width="16" height="16"><circle cx="8" cy="5" r="3.5" fill="#8c2a1f"/><path d="M1 16c0-5 3-7 7-7s7 2 7 7z" fill="#8c2a1f"/></svg>Log in</span>
  </div>
  <nav class="abs main-nav">
    <a class="active" href="#">Home</a><a href="#">Find a Lawyer</a><a href="#">Know your Rights</a><a href="#">News</a><a href="#">Articles</a><a href="#">Contact Us</a>
  </nav>
</header>

<section>
  <div class="abs hero-photo" role="img" aria-label="Photo of a federal court building under a blue sky"></div>
  <div class="abs hero-title">Welcome to Cedar Group</div>
  <form class="abs finder">
    <h2>Find a Lawyer</h2>
    <div class="field"><i><svg width="12" height="12"><circle cx="6" cy="6" r="5" fill="none" stroke="#fff" stroke-width="1.5"/><path d="M3.5 6l2 2 3-4" fill="none" stroke="#fff" stroke-width="1.5"/></svg></i><span>Practice</span></div>
    <div class="field"><i><svg width="10" height="10"><circle cx="5" cy="3" r="2.5" fill="#fff"/><path d="M0 10c0-3 2-4.5 5-4.5s5 1.5 5 4.5z" fill="#fff"/></svg></i><span>Lawyers name</span></div>
    <div class="field"><i><svg width="10" height="10"><rect x="0.5" y="1.5" width="9" height="8" fill="none" stroke="#fff"/><path d="M0.5 4h9" stroke="#fff"/></svg></i><span>Law firm name</span></div>
    <div class="field"><i><svg width="10" height="12"><path d="M5 12S0 6.5 0 4.5a5 5 0 0 1 10 0C10 6.5 5 12 5 12z" fill="#fff"/><circle cx="5" cy="4.5" r="1.7" fill="#8c2a1f"/></svg></i><span>Location</span></div>
    <span class="search-btn">SEARCH <span style="color:#f39c12;font-size:9px">●</span></span>
  </form>
  <div class="abs slider-ctrl">
    <svg width="22" height="12"><path d="M6 2L2 6l4 4" fill="none" stroke="#222" stroke-width="2"/><path d="M15 2l4 4-4 4" fill="none" stroke="#777" stroke-width="2"/></svg>
    <span style="width:1px;height:27px;background:#bbb;margin:0 4px"></span>
    <span class="dot"></span><span class="dot"></span><span class="dot on"></span><span class="dot"></span><span class="dot"></span><span class="dot"></span>
  </div>
</section>

<section class="abs offer">
  <h1>WE OFFER OUR CLIENTS AN <em>EXPERT &amp; GENERAL</em> LEGAL ADVICE.</h1>
  <p>– Check the great feature list why you should buy –</p>
</section>
<a class="abs btn btn-dark cta-learn">Learn More</a>
<span class="abs cta-or">– or –</span>
<a class="abs btn btn-red cta-join">Join with us</a>

<div class="abs band"></div>
<article class="abs feature" style="left:170px">
  <h3><svg width="36" height="22"><circle cx="8" cy="6" r="4" fill="#a23c2e"/><circle cx="28" cy="6" r="4" fill="#a23c2e"/><circle cx="18" cy="5" r="5" fill="#a23c2e"/><path d="M1 22c0-7 3-10 7-10s7 3 7 10zM21 22c0-7 3-10 7-10s7 3 7 10zM10 22c0-8 3-11 8-11s8 3 8 11z" fill="#a23c2e"/></svg>PEOPLE VISITING</h3>
  <p>Serce wisi eturna aliquam volutpat adiscing duisac consequat non dui. Sed eget tortor ut neque scelerisque vehicula pretium eget libero.</p>
  <a class="btn btn-dark">Read More</a>
</article>
<article class="abs feature" style="left:466px">
  <h3><svg width="22" height="22"><path d="M11 1L1 6h20z" fill="#a23c2e"/><rect x="2" y="7" width="18" height="2" fill="#a23c2e"/><rect x="4" y="10" width="3" height="8" fill="#a23c2e"/><rect x="9.5" y="10" width="3" height="8" fill="#a23c2e"/><rect x="15" y="10" width="3" height="8" fill="#a23c2e"/><rect x="1" y="19" width="20" height="3" fill="#a23c2e"/></svg>DOCUMENTATION</h3>
  <p>Serce wisi eturna aliquam volutpat adiscing duisac consequat non dui. Sed eget tortor ut neque scelerisque vehicula pretium eget libero.</p>
  <a class="btn btn-dark">Read More</a>
</article>
<article class="abs feature" style="left:746px">
  <h3><svg width="22" height="22"><path d="M11 2v18M6 20h10M3 5h16" stroke="#a23c2e" stroke-width="2" fill="none"/><path d="M3 5L0 12h6zM19 5l-3 7h6z" fill="none" stroke="#a23c2e" stroke-width="1.5"/></svg>KNOW YOUR RIGHTS</h3>
  <p>Serce wisi eturna aliquam volutpat adiscing duisac consequat non dui. Sed eget tortor ut neque scelerisque vehicula pretium eget libero.</p>
  <a class="btn btn-dark">Read More</a>
</article>

<h2 class="abs section-title" style="left:158px;top:798px">SOLUTIONS OVERVIEW</h2>
<div class="abs solutions-photo" role="img" aria-label="Photo of an official seated in an office beside national flags"></div>
<p class="abs solutions-text">Serce wisi eturna aliquam volutpat adiscing duisac consequat non dui. Sed eget tortor ut neque scelerisque vehicula pretium eget libero. Serce wisi</p>
<a class="abs btn btn-red sol-btn">Read More</a>

<h2 class="abs section-title" style="left:585px;top:792px">LATEST NEWS</h2>
<div class="abs news-box"></div>
<div class="abs news-item" style="top:829px">
  <div class="news-thumb" role="img" aria-label="Photo of hands signing legal papers" style="background:linear-gradient(135deg,#3a2a1e,#c98a55 60%,#e9d4b4)"></div>
  <div><h4>Fusce malesuada orci sed euismod</h4><p>Aenean ultrices turpis. Mauris a nulla<br>quis nisi interdum tempor</p></div>
</div>
<div class="abs news-item" style="top:906px">
  <div class="news-thumb" role="img" aria-label="Photo of a judge's gavel" style="background:linear-gradient(135deg,#8a2a1c,#5a2a18 55%,#c9774a)"></div>
  <div><h4>Fusce malesuada orci sed euismod</h4><p>Aenean ultrices turpis. Mauris a nulla<br>quis nisi interdum tempor</p></div>
</div>
<div class="abs news-item" style="top:982px">
  <div class="news-thumb" role="img" aria-label="Photo of a courthouse facade" style="background:linear-gradient(180deg,#dcdcdc,#c9ad7c 50%,#a88a5a)"></div>
  <div><h4>Fusce malesuada orci sed euismod</h4><p>Aenean ultrices turpis. Mauris a nulla<br>quis nisi interdum tempor</p></div>
</div>

<footer>
  <div class="abs footer"></div>
  <div class="abs footer-links">Home | Find a Lawyer | Know your rights | News | Articles | Contact us</div>
  <div class="abs copyright">Copyright © 2013 Cedar Group. All right reserved.</div>
  <div class="abs social">
    <span style="background:#4fb5e6"></span><span style="background:#3b5aa0"></span><span style="background:#666"></span><span style="background:#e2588b"></span><span style="background:#f2f2f2"></span>
  </div>
  <div class="abs newsletter">NEWS LETTER
    <svg width="26" height="18" style="position:absolute;right:6px;top:3px"><rect x="1" y="1" width="24" height="16" rx="2" fill="#222"/><path d="M2 3l11 8 11-8" fill="none" stroke="#fff" stroke-width="2"/></svg>
  </div>
</footer>

</body>
</html>
```